A friend who listens

find a friend who listens. place holder site:

http://afriendwholistens-example.com/

Coding

Coded - Design and coding required

Number of Pages Required

5+ page

Colors

Designer to choose colors to be used in the design.

```html
<!DOCTYPE html>
<html lang="en">
<head>
<meta charset="utf-8">
<title>A Friend Who Listens</title>
<link href="https://fonts.googleapis.com/css2?family=Poppins:wght@400;500;600;700&family=Open+Sans:wght@400;600&family=Dancing+Script:wght@600&display=swap" rel="stylesheet">
<style>
:root{
  --purple:#5a2a84;
  --purple-dark:#41195f;
  --orange:#f15a24;
  --red:#d8322e;
  --ink:#2b2b35;
  --muted:#6d6d78;
  --light:#f5f3f7;
  --footer:#1d1a26;
  --white:#fff;
}
*{box-sizing:border-box;margin:0;padding:0}
html,body{width:1200px;height:4424px;overflow:hidden}
body{font-family:"Open Sans",sans-serif;color:var(--ink);background:var(--white);position:relative}
h1,h2,h3,h4,.btn,.nav a,.brand{font-family:"Poppins",sans-serif}
.btn{display:inline-block;background:var(--purple);color:var(--white);font-size:11px;font-weight:600;letter-spacing:.5px;padding:9px 22px;border-radius:20px;text-transform:uppercase}
.btn-orange{background:var(--orange)}
.photo{border-radius:2px}
p{font-size:12.5px;line-height:1.75;color:var(--muted)}

/* header */
.topbar{height:72px;position:relative;border-bottom:1px solid #eee}
.topbar .social{position:absolute;left:90px;top:10px;display:flex;gap:5px}
.topbar .social span{width:18px;height:18px;background:var(--orange);border-radius:2px}
.topbar .call{position:absolute;left:90px;top:36px;font-size:10px;color:var(--muted);line-height:1.4}
.topbar .call b{display:block;color:var(--ink);font-size:12px}
.brand{position:absolute;left:50%;top:12px;transform:translateX(-50%);display:flex;align-items:center;gap:10px;color:var(--purple);font-weight:700;font-size:21px;white-space:nowrap}
.brand i{width:34px;height:34px;border-radius:50%;background:var(--orange)}
.topbar .addr{position:absolute;right:90px;top:8px;font-size:10px;color:var(--muted);display:flex;align-items:center;gap:5px}
.topbar .appt{position:absolute;right:90px;top:34px;border-radius:3px;padding:8px 16px;font-size:10px}
.nav{height:40px;background:var(--orange);display:flex;align-items:center;padding:0 90px;gap:30px}
.nav a{color:var(--white);font-size:11px;font-weight:500;text-decoration:none;text-transform:uppercase}
.nav a.active{background:rgba(255,255,255,.2);padding:12px 14px}
.nav .login{margin-left:auto}

/* hero */
.hero{position:relative;height:488px;background:var(--light);overflow:hidden}
.hero .photo{position:absolute;left:0;top:0;width:720px;height:488px;background:linear-gradient(120deg,#d9d4cf,#f1ede9 45%,#c9bfb6)}
.hero .copy{position:absolute;left:770px;top:120px;width:390px}
.script{font-family:"Dancing Script",cursive;color:var(--purple);font-size:34px;line-height:1}
.hero h1{font-size:36px;font-weight:700;color:var(--ink);line-height:1.2;margin:4px 0 14px;white-space:nowrap}
.hero h1 em{font-style:normal;color:var(--orange)}
.hero p{font-size:11.5px;margin-bottom:18px;width:340px}
.hero svg{position:absolute;left:0;bottom:0}

/* welcome */
.welcome{position:relative;height:400px}
.welcome .copy{position:absolute;left:90px;top:110px;width:500px}
.kicker{color:var(--orange);font-size:13px;font-weight:600;font-family:"Poppins",sans-serif}
.welcome h2{color:var(--purple);font-size:28px;font-weight:600;margin:2px 0 14px}
.welcome p{margin-bottom:22px}
.welcome .ring{position:absolute;left:720px;top:20px}
.welcome .circle-photo{position:absolute;left:760px;top:60px;width:300px;height:300px;border-radius:50%;background:linear-gradient(135deg,#8da3b5,#c7d3dc 50%,#5f6f7d)}

/* services */
.section-head{text-align:center}
.section-head .kicker{font-size:12px}
.section-head > h2{font-size:32px;font-weight:500;color:var(--ink);margin:2px 0 10px}
.section-head > p{width:620px;margin:0 auto;font-size:11px}
.services-head{height:200px;padding-top:60px}
.service{position:relative;height:390px}
.service .photo{position:absolute;top:0;width:380px;height:260px}
.service .copy{position:absolute;top:80px;width:420px}
.service.left .photo{left:90px}
.service.left .copy{left:660px}
.service.right .photo{left:730px}
.service.right .copy{left:90px;top:40px}
.service h3{font-size:20px;font-weight:500;margin-bottom:12px}
.service p{font-size:11px;margin-bottom:10px}
.service .btn{margin-top:6px}

/* testimonial */
.testimonial{height:360px;background:var(--purple);text-align:center;color:var(--white);padding-top:46px;margin-top:20px}
.testimonial .kicker{color:#f2c9ee;font-weight:500}
.testimonial h2{font-size:32px;font-weight:500;margin-bottom:16px}
.avatar{width:80px;height:80px;border-radius:50%;margin:0 auto;background:linear-gradient(135deg,#e8d6cc,#b89581);border:4px solid var(--white)}
.stars{color:#ffb400;font-size:14px;letter-spacing:2px;margin:8px 0 10px}
.testimonial p{color:#e6dcef;width:820px;margin:0 auto;font-size:11px}
.testimonial .name{margin-top:14px;font-weight:600;font-size:13px;font-family:"Poppins",sans-serif}

/* blog */
.blog{height:620px;padding-top:60px}
.cards{display:flex;gap:30px;margin:36px 0 0 90px;text-align:left}
.card{width:320px;flex:none}
.card .photo{position:relative;height:196px}
.card .date{position:absolute;right:12px;bottom:14px;width:40px;height:44px;background:var(--orange);color:var(--white);font:600 13px/1.1 "Poppins",sans-serif;text-align:center;padding-top:6px}
.card .date small{display:block;font-size:9px;font-weight:400}
.card h4{font-size:14px;font-weight:600;margin:14px 0 6px;line-height:1.35;color:var(--ink)}
.card p{width:100%;font-size:10.5px;line-height:1.6;margin:0 0 14px}

/* footer */
.footer{position:absolute;left:0;top:3864px;width:1200px;height:560px;background:var(--footer);color:var(--white)}
.cta{position:absolute;left:0;top:-4px;width:1200px;height:44px;display:flex;justify-content:center;gap:26px;background:linear-gradient(90deg,transparent 0,transparent 200px,var(--white) 200px,var(--white) 960px,var(--purple) 1080px)}
.cta .btn{font-size:13px;padding:13px 0;width:150px;text-align:center;border-radius:24px;margin-top:0}
.cta .red{background:var(--red)}
.footer h2{position:absolute;left:90px;top:96px;font-size:28px;font-weight:500}
.form{position:absolute;left:90px;top:156px;width:580px;display:grid;grid-template-columns:1fr 1fr;column-gap:40px;row-gap:26px}
.field{font-size:10px;color:#c9c6d2;border-bottom:1px solid #4a4658;padding-bottom:18px}
.field.wide{grid-column:1/3;padding-bottom:70px}
.form .btn{grid-column:2;justify-self:end;margin-top:-6px}
.contact{position:absolute;left:760px;top:156px;width:340px}
.contact .item{display:flex;gap:12px;margin-bottom:26px}
.contact .icon{width:28px;height:28px;border-radius:50%;background:var(--orange);flex:none;display:flex;align-items:center;justify-content:center}
.contact h4{font-size:12px;font-weight:600;color:var(--orange);margin-bottom:3px}
.contact p{color:#c9c6d2;font-size:10.5px;line-height:1.5}
.footer .social{position:absolute;left:0;right:0;top:490px;display:flex;justify-content:center;gap:8px}
.footer .social span{width:22px;height:22px;border-radius:3px;background:#2f6fd1}
.footer .social span+span{background:#3a3648}
.copyright{position:absolute;left:0;right:0;top:530px;text-align:center;font-size:10px;color:#8f8b9c}
.copyright b{color:var(--orange);font-weight:600}
</style>
</head>
<body>

<header class="topbar">
  <div class="social"><span></span><span></span><span></span><span></span></div>
  <div class="call">Call Us Today <b>+1 (555) 014-2290</b></div>
  <div class="brand"><i></i>A Friend Who Listens</div>
  <div class="addr">
    <svg width="10" height="12" viewBox="0 0 10 12"><path d="M5 0a4 4 0 0 0-4 4c0 3 4 8 4 8s4-5 4-8a4 4 0 0 0-4-4zm0 5.5A1.5 1.5 0 1 1 5 2.5a1.5 1.5 0 0 1 0 3z" fill="#f15a24"/></svg>
    48 Quiet Lane, Suite 12, Brookhaven
  </div>
  <span class="btn btn-orange appt">Book An Appointment</span>
</header>
<nav class="nav">
  <a class="active">Home</a><a>About Us</a><a>Services</a><a>Blog</a><a>Contact Us</a>
  <a class="login">Login / Register</a>
</nav>

<section class="hero">
  <div class="photo" role="img" aria-label="Photo of two women sitting and talking together"></div>
  <div class="copy">
    <div class="script">Benefits of</div>
    <h1>Talking to <em>Someone</em></h1>
    <p>Talking to a friend who listens can lift a heavy load from your mind. Share what you carry and feel lighter today.</p>
    <span class="btn">Get Started</span>
  </div>
  <svg width="1200" height="90" viewBox="0 0 1200 90" preserveAspectRatio="none">
    <path d="M0 70 Q600 -10 1200 40 L1200 90 L0 90Z" fill="#fff"/>
    <path d="M600 30 Q900 10 1200 28" stroke="#5a2a84" stroke-width="10" fill="none"/>
    <path d="M700 28 Q950 14 1200 40" stroke="#f15a24" stroke-width="5" fill="none"/>
  </svg>
</section>

<section class="welcome">
  <div class="copy">
    <div class="kicker">Welcome To</div>
    <h2>A Friend Who Listens</h2>
    <p>Here you will always find a patient ear. We believe every person deserves a calm space to speak freely, to be heard without judgement and to leave feeling understood. Our listeners are kind, caring and ready whenever you need them, by day or by night.</p>
    <span class="btn">Read More</span>
  </div>
  <svg class="ring" width="380" height="380" viewBox="0 0 380 380">
    <path d="M60 110 A160 160 0 0 1 330 120" stroke="#5a2a84" stroke-width="16" fill="none"/>
    <path d="M40 200 A150 150 0 0 0 190 350" stroke="#f15a24" stroke-width="8" fill="none"/>
  </svg>
  <div class="circle-photo" role="img" aria-label="Photo of two friends talking face to face"></div>
</section>

<section class="section-head services-head">
  <div class="kicker">What We Do</div>
  <h2>Our Services</h2>
  <p>Gentle support for every kind of day. Choose the way of talking that feels right for you and we will be there to listen.</p>
</section>

<section class="service left">
  <div class="photo" role="img" aria-label="Photo of a support group sitting in a circle" style="background:linear-gradient(135deg,#6e6158,#b5a596 55%,#4b423c)"></div>
  <div class="copy">
    <h3>Benefits of Talking To Someone</h3>
    <p>Putting your thoughts into words can ease worry and bring clarity. A listener helps you untangle feelings, see things more calmly and find your own next step with confidence and care.</p>
    <span class="btn">Read More</span>
  </div>
</section>
<section class="service right">
  <div class="copy">
    <h3>Sorting Through Your Feelings</h3>
    <p>Talking out loud about what is going on in your heart can help you sort it. Our listeners give you the time and room to explore every feeling gently.</p>
    <p>Saying things out loud often makes them less scary and is the first step towards feeling better and more in control of your day.</p>
    <p>Simply talking helps more than most people expect.</p>
    <span class="btn">Read More</span>
  </div>
  <div class="photo" role="img" aria-label="Photo of two women in a quiet conversation on a sofa" style="background:linear-gradient(135deg,#e9dcd0,#c8ad98 55%,#f3ece5)"></div>
</section>
<section class="service left">
  <div class="photo" role="img" aria-label="Photo of a counsellor listening to a client in a bright room" style="background:linear-gradient(135deg,#d7e0e6,#9fb0bb 55%,#eef2f4)"></div>
  <div class="copy">
    <h3>Putting Things In Perspective</h3>
    <p>When worries keep circling in your head it can be hard to see the whole picture. Sharing them with someone who cares can help you step back and look again.</p>
    <p>Sometimes a fresh point of view is all it takes to make a problem feel smaller and more manageable.</p>
    <span class="btn">Read More</span>
  </div>
</section>
<section class="service right">
  <div class="copy">
    <h3>Releasing Tension</h3>
    <p>Talking about your day can release built up stress. Letting go of tension in a safe space helps your body and mind relax and recover.</p>
    <p>Saying things out loud often makes them lighter and gives you room to breathe again with ease.</p>
    <p>A short chat can change the whole feel of a day.</p>
    <span class="btn">Read More</span>
  </div>
  <div class="photo" role="img" aria-label="Photo of a small group sharing stories in a dim room" style="background:linear-gradient(135deg,#4a423f,#8a7a70 55%,#2f2a28)"></div>
</section>

<section class="testimonial">
  <div class="kicker">What Our</div>
  <h2>Customer Say's</h2>
  <div class="avatar" role="img" aria-label="Portrait photo of the reviewer"></div>
  <div class="stars">★★★★★</div>
  <p>I did not know how much I needed to be heard until I found this place. Every conversation left me calmer and clearer about what to do next. The listeners are warm, patient and never rush you. I would recommend it to anyone who feels alone with their thoughts or simply needs a kind voice at the end of a long day.</p>
  <div class="name">Miss. Jana Porterly</div>
</section>

<section class="section-head blog">
  <div class="kicker">Our Blog</div>
  <h2>Recent Article Post</h2>
  <div class="cards">
    <article class="card">
      <div class="photo" role="img" aria-label="Photo of a group meeting in a classroom" style="background:linear-gradient(135deg,#5d5249,#a69586)"><div class="date">18<small>Mar</small></div></div>
      <h4>Lorem ipsum dolor sit amet, consectetur adipiscing elit</h4>
      <p>Sed do eiusmod tempor incididunt ut labore et dolore magna aliqua ut enim ad minim.</p>
      <span class="btn">Read More</span>
    </article>
    <article class="card">
      <div class="photo" role="img" aria-label="Photo of a family talking at a table" style="background:linear-gradient(135deg,#c9b7a4,#8e7562)"><div class="date">22<small>Mar</small></div></div>
      <h4>Lorem ipsum dolor sit amet, consectetur adipiscing elit</h4>
      <p>Sed do eiusmod tempor incididunt ut labore et dolore magna aliqua ut enim ad minim.</p>
      <span class="btn">Read More</span>
    </article>
    <article class="card">
      <div class="photo" role="img" aria-label="Photo of people chatting in an office" style="background:linear-gradient(135deg,#b3a79d,#6d625a)"><div class="date">27<small>Mar</small></div></div>
      <h4>Lorem ipsum dolor sit amet, consectetur adipiscing elit</h4>
      <p>Sed do eiusmod tempor incididunt ut labore et dolore magna aliqua ut enim ad minim.</p>
      <span class="btn">Read More</span>
    </article>
  </div>
</section>

<footer class="footer">
  <div class="cta">
    <span class="btn btn-orange">Live Chat</span>
    <span class="btn red">Services</span>
    <span class="btn">Get A Free Quote</span>
  </div>
  <h2>We're Here to Help!</h2>
  <form class="form">
    <div class="field">Name</div>
    <div class="field">E-mail Address</div>
    <div class="field">Phone</div>
    <div class="field">Preferred Date</div>
    <div class="field wide">Message</div>
    <span class="btn">Send Message</span>
  </form>
  <div class="contact">
    <div class="item">
      <span class="icon"><svg width="10" height="12" viewBox="0 0 10 12"><path d="M5 0a4 4 0 0 0-4 4c0 3 4 8 4 8s4-5 4-8a4 4 0 0 0-4-4zm0 5.5A1.5 1.5 0 1 1 5 2.5a1.5 1.5 0 0 1 0 3z" fill="#fff"/></svg></span>
      <div><h4>Office Location</h4><p>48 Quiet Lane, Suite 12<br>Brookhaven</p></div>
    </div>
    <div class="item">
      <span class="icon"><svg width="12" height="12" viewBox="0 0 12 12"><path d="M2.5 0.5l2 2.5-1.2 1.5a7 7 0 0 0 4.2 4.2L9 7.5l2.5 2-1.5 2C5 11.5 0.5 7 0.5 2z" fill="#fff"/></svg></span>
      <div><h4>Office Phone</h4><p>+1 (555) 014-2290<br>+1 (555) 014-2291</p></div>
    </div>
    <div class="item">
      <span class="icon"><svg width="12" height="10" viewBox="0 0 12 10"><rect x="0.5" y="0.5" width="11" height="9" fill="none" stroke="#fff"/><path d="M0.5 0.5L6 5.5l5.5-5" fill="none" stroke="#fff"/></svg></span>
      <div><h4>Office Email</h4><p>hello@afriendwholistens-example.com</p></div>
    </div>
  </div>
  <div class="social"><span></span><span></span><span></span><span></span></div>
  <div class="copyright">Copyright © 2024 <b>A Friend Who Listens</b>. All Rights Reserved.</div>
</footer>

</body>
</html>
```